EXTENDED Store hours to serve your healthcare needs

I'M LOOKING FOR A NICE FLYER THAT SHOWS THE FOLLOWING INFORMATION:

Logo
address
tel phone and fax
email address

Extending our hours to meet the growing healthcare needs of our community. Fast delivery service!

Monday - Thursday 10am-midnight
Friday 10am-4pm
Saturday - Motzei Shabbos till midnight
Sunday 10am-7pm

Target Market(s)

Community

Industry/Entity Type

Pharmacy

Requirements
Must have
• Extended hours
• personal care
• expert advice
• superior service
Nice to have
• Looking for no people pictures
• Eye popping design
• Classic modern clean design
Should not have
• store description is services
• And should not say Fiirst to open and last to close

```html
<!DOCTYPE html>
<html lang="en">
<head>
<meta charset="utf-8">
<title>K. Lane Pharmacy – New Extended Hours</title>
<link rel="stylesheet" href="https://fonts.googleapis.com/css2?family=Lexend:wght@400;500;600&family=Kaushan+Script&family=Oswald:wght@400;500&display=swap">
<style>
  :root{
    --blue:#2f56aa;
    --sky:#29abe2;
    --sky-dark:#1a6fa3;
    --red:#c1222b;
    --red-text:#d42a2a;
    --ink:#1e1e24;
    --band:#a7adb8;
    --band-light:#c9cdd4;
    --paper:#ffffff;
    --page:#e9e9ea;
  }
  *{margin:0;padding:0;box-sizing:border-box}
  html,body{width:1200px;height:1076px;overflow:hidden;background:var(--page)}
  .flyer{
    position:absolute;left:247px;top:38px;width:705px;height:1000px;
    background:var(--paper);overflow:hidden;
    box-shadow:0 6px 24px rgba(0,0,0,.18);
    font-family:"Lexend",sans-serif;color:var(--ink);
  }
  .flyer > svg{position:absolute;left:0;top:0}
  .brand{position:absolute;left:22px;top:52px;display:flex;align-items:center;gap:16px}
  .brand-dot{width:58px;height:58px;border-radius:50%;background:var(--blue)}
  .brand-name{font-family:"Lexend",sans-serif;font-weight:600;font-size:44px;color:var(--red);letter-spacing:.5px}
  .new-badge{
    position:absolute;left:44px;top:410px;width:112px;height:112px;border-radius:50%;
    background:radial-gradient(circle at 50% 30%,#e8373f 0%,var(--red) 70%);
    border:4px solid #e4e4e6;display:flex;align-items:center;justify-content:center;
    font-family:"Lexend",sans-serif;font-weight:600;font-size:30px;color:#fff;
  }
  .headline{
    position:absolute;left:14px;top:528px;
    font-family:"Kaushan Script",cursive;font-size:44px;color:var(--blue);white-space:nowrap;
  }
  .headline .big{font-size:50px}
  .day{
    position:absolute;height:40px;padding:0 18px;
    background:var(--sky);color:var(--red-text);
    font-family:"Oswald",sans-serif;font-variant:small-caps;font-size:27px;line-height:40px;
    box-shadow:inset 0 -4px 0 rgba(0,0,0,.08);
  }
  .day::before,.day::after{content:"";position:absolute;top:-6px;border-bottom:6px solid var(--sky-dark)}
  .day::before{left:0;border-left:8px solid transparent}
  .day::after{right:0;border-right:8px solid transparent}
  .time{position:absolute;font-size:26px;font-weight:400;line-height:27px;white-space:nowrap}
  .services{position:absolute;left:20px;top:850px;width:300px;list-style:none}
  .services li{font-size:15px;line-height:22px;color:var(--blue);font-weight:500}
  .services .delivery{color:var(--red);font-weight:600;font-size:16px;margin-bottom:2px}
  .contact{position:absolute;left:342px;display:flex;align-items:center;gap:8px;font-size:14px;white-space:nowrap}
  .contact.phone{font-size:15px}
  .contact svg{flex:none}
</style>
</head>
<body>
<main class="flyer">
  <svg class="waves" width="705" height="1000" viewBox="0 0 705 1000" aria-hidden="true">
    <rect x="0" y="180" width="705" height="420" fill="#f1f2f4"/>
    <path fill="var(--blue)" d="M0,198 C180,240 380,190 520,130 C600,100 660,92 705,92 L705,108 C640,112 580,132 520,162 C380,228 170,268 0,240 Z"/>
    <path fill="var(--red)" d="M0,338 C150,330 280,372 400,442 C510,506 610,542 705,536 L705,554 C610,560 500,526 390,462 C270,392 150,352 0,360 Z"/>
    <path fill="var(--blue)" d="M0,360 C150,352 270,392 390,462 C500,526 610,560 705,554 L705,572 C600,580 490,546 380,482 C262,414 150,376 0,382 Z"/>
    <polygon fill="var(--band-light)" points="505,629 705,629 705,800 462,832"/>
    <polygon fill="var(--band)" points="0,591 548,591 465,831 0,831"/>
    <path fill="#eceef1" d="M0,831 L465,831 L705,800 L705,878 C480,973 200,985 0,928 Z"/>
    <path fill="none" stroke="#9a9da3" stroke-width="9" d="M0,934 C200,989 480,979 705,884"/>
    <path fill="var(--red)" d="M0,958 C220,1005 480,992 705,906 L705,1000 L0,1000 Z"/>
  </svg>

  <svg width="705" height="1000" viewBox="0 0 705 1000" role="img" aria-label="Photo of colourful tablets and capsules spilling from a glass bowl">
    <defs>
      <linearGradient id="pills" x1="0" y1="0" x2="1" y2="1">
        <stop offset="0" stop-color="#e9e9ec"/>
        <stop offset=".45" stop-color="#d8b6c0"/>
        <stop offset=".75" stop-color="#e6d6c8"/>
        <stop offset="1" stop-color="#eeeef0"/>
      </linearGradient>
    </defs>
    <path fill="url(#pills)" d="M0,240 C170,268 380,228 520,162 C580,132 640,112 705,108 L705,536 C610,542 510,506 400,442 C280,372 150,330 0,338 Z"/>
  </svg>

  <div class="brand">
    <span class="brand-dot"></span>
    <span class="brand-name">K. Lane Pharmacy</span>
  </div>

  <div class="new-badge">NEW</div>
  <h1 class="headline">New <span class="big">EXTENDED</span> Hours</h1>

  <div class="day" style="left:16px;top:621px">Mon- Thur</div>
  <p class="time" style="left:8px;top:674px">10am-midnight</p>
  <div class="day" style="left:16px;top:711px">Saturday</div>
  <p class="time" style="left:16px;top:764px">Motzei -midnight<br>Shabbos</p>

  <div class="day" style="left:306px;top:614px">Friday</div>
  <p class="time" style="left:307px;top:671px">10am-4pm</p>
  <div class="day" style="left:306px;top:706px">Sunday</div>
  <p class="time" style="left:306px;top:760px">10am-7pm</p>

  <svg style="left:552px;top:641px" width="126" height="148" viewBox="0 0 126 148" role="img" aria-label="Illustration of a silver alarm clock">
    <defs>
      <radialGradient id="clock" cx=".45" cy=".4" r=".6">
        <stop offset="0" stop-color="#f7f7f7"/>
        <stop offset="1" stop-color="#9ea2a8"/>
      </radialGradient>
    </defs>
    <circle cx="63" cy="80" r="60" fill="url(#clock)"/>
  </svg>

  <ul class="services">
    <li class="delivery">Fast delivery service!</li>
    <li>Personal care · Expert advice</li>
    <li>Superior service</li>
  </ul>

  <div class="contact phone" style="top:850px">
    <svg width="22" height="22" viewBox="0 0 24 24" aria-hidden="true"><rect x="1" y="1" width="22" height="22" rx="4" fill="var(--red)" stroke="var(--blue)" stroke-width="2"/><path d="M8 6 L10 6 L11 9 L9.5 10 C10.3 12 11.8 13.6 14 14.5 L15 13 L18 14 L18 16 C18 17 17 18 16 18 C10 17 7 13 6 8 C6 7 7 6 8 6 Z" fill="#fff"/></svg>
    <span>Tel 718-555-0142 &nbsp;|&nbsp; Fax 718-555-0143</span>
  </div>
  <div class="contact" style="top:882px">
    <svg width="22" height="22" viewBox="0 0 24 24" aria-hidden="true"><rect x="1" y="1" width="22" height="22" rx="4" fill="var(--red)" stroke="var(--blue)" stroke-width="2"/><path d="M12 5 C9 5 7.5 7 7.5 9.3 C7.5 12.5 12 19 12 19 C12 19 16.5 12.5 16.5 9.3 C16.5 7 15 5 12 5 Z" fill="none" stroke="#fff" stroke-width="1.6"/><circle cx="12" cy="9.5" r="1.7" fill="#fff"/></svg>
    <span>48 Orchard Ave Brooklyn, NY 11206</span>
  </div>
  <div class="contact" style="top:914px">
    <svg width="22" height="22" viewBox="0 0 24 24" aria-hidden="true"><rect x="1" y="1" width="22" height="22" rx="4" fill="var(--red)" stroke="var(--blue)" stroke-width="2"/><rect x="6" y="8" width="12" height="9" fill="#fff"/><path d="M6 8 L12 13 L18 8" fill="none" stroke="var(--red)" stroke-width="1.4"/></svg>
    <span>klanepharmacy@mail.com</span>
  </div>
</main>
</body>
</html>
```